Sales Brochure- Generic Line Card 215mm x 140mm

Design a double-sided brochure similar to the attached sample. Cover Page contains a logo and theme that never changes. However, the background picture and the description text on the lower corner will be changed to advertise multiple services. Reverse-side contains Detailed Descriptive text related to the picture on Cover Page as well as Logo and Contact information for the business. Use the Ridgeline Controls website www.ridgelinecontrols.ca for theme, color and contact information. Also, use attached business card design for theme to match. Use the supplied logo. SIZE 215mm x 140mm

Font styles to use
Sans Serif

Colors

Designer to choose colors to be used in the design.

Requirements
Must have
• Look Similar to Sample Brochure but include Ridgeline Controls theme and colors

```html
<!DOCTYPE html>
<html lang="en">
<head>
<meta charset="utf-8">
<title>Ridgeline Controls – Swiss CNC Line Card</title>
<link href="https://fonts.googleapis.com/css2?family=Questrial&family=Montserrat:wght@700&display=swap" rel="stylesheet">
<style>
  :root {
    --teal: #1a9aa3;
    --teal-bright: #2ec6d6;
    --teal-deep: #0f8c98;
    --ink: #1f2124;
    --charcoal: #2a2c30;
    --white: #ffffff;
    --steel-light: #e4e6e8;
    --steel-mid: #a9adb1;
  }
  * { margin: 0; padding: 0; box-sizing: border-box; }
  html, body { width: 839px; height: 1200px; overflow: hidden; background: var(--white); }
  body { position: relative; font-family: "Questrial", sans-serif; }

  .card {
    position: absolute;
    left: 29px;
    box-shadow: 3px 5px 8px rgba(0,0,0,0.45);
    overflow: hidden;
  }

  /* ---- Front cover ---- */
  .card--front { top: 44px; width: 783px; height: 508px; background: var(--charcoal); }
  .front__photo {
    position: absolute; left: 0; top: 0; width: 783px; height: 484px;
    background: linear-gradient(100deg, #d9dbdd 0%, #c4c7ca 35%, #8e9296 55%, #5b5f63 70%, #b7babd 85%, #6d7175 100%);
  }
  .front__chevron { position: absolute; left: 0; top: 50px; }
  .front__strip {
    position: absolute; left: 0; top: 484px; width: 783px; height: 24px;
    background: linear-gradient(90deg, #2b2d31, #1d1f22);
  }
  .logo-pill {
    position: absolute; display: flex; align-items: center; gap: 8px;
    background: var(--white);
    border-radius: 0 24px 24px 0;
    padding-left: 14px;
  }
  .logo-pill__mark { width: 14px; height: 14px; background: var(--teal); flex: none; }
  .logo-pill__name {
    font-family: "Questrial", sans-serif; color: var(--ink);
    letter-spacing: 0.5px; white-space: nowrap;
  }
  .card--front .logo-pill { left: 0; top: 8px; width: 231px; height: 44px; }
  .card--front .logo-pill__name { font-size: 21px; }

  .service-tag {
    position: absolute; right: 0; top: 414px; width: 260px; height: 52px;
    background: var(--white); border-radius: 26px 0 0 26px;
    display: flex; align-items: center; justify-content: center;
  }
  .service-tag__title {
    font-family: "Montserrat", sans-serif; font-weight: 700;
    font-size: 27px; color: var(--teal); padding-left: 20px;
  }

  /* ---- Reverse ---- */
  .card--back { top: 616px; width: 785px; height: 512px; background: var(--ink); }
  .back__photo {
    position: absolute; right: 0; top: 0; width: 420px; height: 454px;
    background: linear-gradient(90deg, rgba(31,33,36,1) 0%, rgba(58,61,65,0.9) 40%, rgba(70,73,77,0.85) 70%, rgba(48,51,55,1) 100%);
  }
  .back__content { position: absolute; left: 29px; top: 42px; width: 700px; color: var(--white); }
  .back__heading {
    font-family: "Montserrat", sans-serif; font-weight: 700;
    font-size: 28px; color: var(--teal); letter-spacing: -0.3px; line-height: 1;
  }
  .back__intro { margin-top: 14px; font-size: 14.3px; line-height: 22px; }
  .back__list { margin-top: 16px; margin-left: 11px; list-style: none; font-size: 14.3px; line-height: 22px; }
  .back__list li::before { content: "•"; margin-right: 6px; }

  .contact-band { position: absolute; left: 0; top: 454px; width: 785px; height: 58px; }
  .contact-band__shape { position: absolute; left: 0; top: 0; }
  .card--back .logo-pill { left: 0; top: 11px; width: 180px; height: 36px; padding-left: 10px; gap: 6px; }
  .card--back .logo-pill__mark { width: 11px; height: 11px; }
  .card--back .logo-pill__name { font-size: 16px; }
  .contact-band__text {
    position: absolute; left: 190px; width: 540px; top: 12px;
    text-align: center; color: var(--white); font-size: 12.2px; line-height: 17px;
  }
  .contact-band__web { font-size: 13px; }
</style>
</head>
<body>

<section class="card card--front">
  <div class="front__photo" role="img" aria-label="Close-up photo of a Swiss CNC lathe: spindle chuck holding a small part beside a gang of rotating cutting tools"></div>
  <svg class="front__chevron" width="104" height="482" viewBox="0 0 104 482" aria-hidden="true">
    <defs>
      <linearGradient id="chevronFill" x1="0" y1="0" x2="1" y2="0">
        <stop offset="0" stop-color="#2cb8c6"/>
        <stop offset="1" stop-color="#1c9aa6"/>
      </linearGradient>
    </defs>
    <polygon points="0,0 104,0 104,375 51,430 0,375" fill="url(#chevronFill)" opacity="0.92"/>
  </svg>
  <div class="logo-pill">
    <span class="logo-pill__mark"></span>
    <span class="logo-pill__name">Ridgeline Controls</span>
  </div>
  <div class="service-tag"><span class="service-tag__title">SWISS CNC</span></div>
  <div class="front__strip"></div>
</section>

<section class="card card--back">
  <div class="back__photo" role="img" aria-label="Faded background photo of the Swiss CNC tooling"></div>
  <div class="back__content">
    <h1 class="back__heading">SWISS MACHINING</h1>
    <p class="back__intro">Swiss machining (also known as “screw machining”) is the most effective way to produce small parts like pins, screws, nuts, washers and high volume parts. The Swiss machine utilizes a simultaneous machining method where multiple cutting processes occur at the same time. By simultaneously machining different features of a small part the process is dramatically quicker than CNC.</p>
    <ul class="back__list">
      <li>Swiss Machines up to 32mm (1.26”) Dia.</li>
      <li>Swiss Multi-Axis up to 8 Simultaneous Processes</li>
      <li>“Lights-out” Production</li>
      <li>High Volume Production and Inventory Consignment</li>
      <li>Custom Screws, Bolts, Pins and Fittings</li>
      <li>Shear Screws and Shear Tension Strength Testing</li>
      <li>Equipment and Machinery Fittings</li>
      <li>Cosmetic Fasteners and Glass Mounting Hardware</li>
      <li>Swiss CAD/CAM Design and Programming</li>
    </ul>
  </div>
  <div class="contact-band">
    <svg class="contact-band__shape" width="785" height="58" viewBox="0 0 785 58" aria-hidden="true">
      <defs>
        <linearGradient id="bandFill" x1="0" y1="0" x2="1" y2="0">
          <stop offset="0" stop-color="#0f8c98"/>
          <stop offset="0.5" stop-color="#2ec6d6"/>
          <stop offset="1" stop-color="#16a3b0"/>
        </linearGradient>
      </defs>
      <polygon points="0,0 697,0 785,46 785,58 0,58" fill="url(#bandFill)"/>
    </svg>
    <div class="logo-pill">
      <span class="logo-pill__mark"></span>
      <span class="logo-pill__name">Ridgeline Controls</span>
    </div>
    <p class="contact-band__text">
      1420 Birchwood Rd NW - Calgary, AB - T2K 4R7 &nbsp;|&nbsp; Ph : 403 555 0142 &nbsp;|&nbsp; Fax : 888 555 0187<br>
      <span class="contact-band__web">www.ridgelinecontrols.ca</span>
    </p>
  </div>
</section>

</body>
</html>
```